Flyer Design for an electrical and security company trying to build local customers

I need a flyer design for a new company based in Sans Souci, Sydney 2219 called "Harbor Quill Dune Electrical and Security" also "HQD Electrical and Security". We are electrical contractors who are looking for more local work including emergency service calls and any project work including renovations or new constructions in the local area. I would like everyone in the area to know I am new and that I am available 24 hours a day 7 days a week. I would like to see designs that use the logo colours. Would also like the font of the entire design to be "juice bold".

Electrical

• juice bold

Requirements
Must have
• Must use the colours of the original logo and also have the information from the rear of the card. Must also have services buttons like the website picture attached.

```html
<!DOCTYPE html>
<html lang="en">
<head>
<meta charset="UTF-8">
<title>Harbor Quill Dune Electrical and Security – Our Services</title>
<link href="https://fonts.googleapis.com/css2?family=Arvo&family=Varela+Round&family=Arimo:wght@400;700&display=swap" rel="stylesheet">
<style>
  :root {
    --orange: #f26522;
    --orange-text: #f15a24;
    --blue: #4fc3f1;
    --white: #ffffff;
    --ink: #1d1d1b;
  }
  * { margin: 0; padding: 0; box-sizing: border-box; }
  html, body { width: 1200px; height: 850px; overflow: hidden; background: var(--white); }
  .flyer { position: relative; width: 1200px; height: 850px; overflow: hidden; background: var(--white); font-family: "Varela Round", sans-serif; }

  .orange-field { position: absolute; left: 0; top: 0; width: 1200px; height: 690px; background: var(--orange); }
  .service-panel { position: absolute; left: 0; top: 110px; width: 1188px; height: 576px; background: var(--white); border-radius: 120px 0 110px 0; }

  .header { position: absolute; left: 0; top: 0; width: 1200px; text-align: center; color: var(--white); }
  .header-title { margin-top: 16px; font-size: 36px; font-weight: 400; letter-spacing: 0.5px; }
  .header-rule { width: 470px; margin: 4px auto 0; border-top: 1px dashed var(--white); }
  .header-lead { margin-top: 6px; font-family: "Arimo", sans-serif; font-weight: 700; font-size: 15.5px; line-height: 19px; color: var(--ink); }

  .service { position: absolute; display: flex; align-items: center; height: 72px; }
  .service-tile { width: 71px; height: 71px; background: var(--blue); border-radius: 4px 36px 4px 36px; flex: none; display: flex; align-items: center; justify-content: center; }
  .service-tile svg { width: 46px; height: 46px; }
  .ico { fill: none; stroke: var(--white); stroke-width: 2.4; stroke-linecap: round; stroke-linejoin: round; }
  .ico-fill { fill: var(--white); stroke: none; }
  .ico-text { fill: var(--white); font-family: "Arimo", sans-serif; font-weight: 700; font-size: 10px; }
  .service-name { font-family: "Arvo", serif; font-size: 23.5px; color: var(--orange-text); white-space: nowrap; position: absolute; }

  .col-1 { left: 55px; } .col-1 .service-name { left: 98px; }
  .col-2 { left: 508px; } .col-2 .service-name { left: 92px; }
  .col-3 { left: 818px; } .col-3 .service-name { left: 96px; }
  .row-1 { top: 130px; } .row-2 { top: 224px; } .row-3 { top: 315px; }
  .row-4 { top: 409px; } .row-5 { top: 501px; } .row-6 { top: 596px; }

  .sectors { position: absolute; left: 20px; top: 703px; font-size: 19px; color: var(--ink); }
  .sectors em { font-style: normal; color: var(--orange-text); }

  .contact-bar { position: absolute; left: 0; top: 744px; width: 1012px; height: 106px; background: var(--blue); border-radius: 0 60px 0 0; }
  .call-label { position: absolute; left: 22px; top: 8px; font-size: 22px; color: var(--white); }
  .call-number { position: absolute; left: 18px; top: 34px; font-family: "Arimo", sans-serif; font-weight: 700; font-size: 56px; color: var(--white); letter-spacing: 1px; }
  .website { position: absolute; left: 430px; top: 40px; font-family: "Arimo", sans-serif; font-size: 42px; color: var(--ink); }

  .brand { position: absolute; left: 1030px; top: 712px; width: 160px; display: flex; align-items: flex-start; gap: 8px; }
  .brand-dot { width: 14px; height: 14px; border-radius: 50%; background: var(--blue); flex: none; margin-top: 5px; }
  .brand-name { font-size: 20px; line-height: 24px; color: var(--orange); }
</style>
</head>
<body>
<main class="flyer">
  <div class="orange-field"></div>
  <div class="service-panel"></div>

  <header class="header">
    <h1 class="header-title">Our Services</h1>
    <div class="header-rule"></div>
    <p class="header-lead">We do All House renovations, Construction, Commercial, 24 Hour Emergency Service,<br>New Installations, Repairs, Maintenance, Home Theatre &amp; so on...</p>
  </header>

  <section class="services">
    <div class="service col-1 row-1"><div class="service-tile" role="img" aria-label="Phone and clock icon"><svg viewBox="0 0 40 40"><path class="ico" d="M33 14a14 14 0 1 0 1 10"/><path class="ico-fill" d="M9 13c1-1 2-1 3 0l2 3c.5 1 0 2-1 2.5 1 3 3 5 6 6 .5-1 1.5-1.5 2.5-1l3 2c1 1 1 2 0 3-2 2-5 2-8 0-4-3-7-6-8.5-10-1-2-.5-4 1-5.5z"/><text class="ico-text" x="17" y="19">24</text></svg></div><span class="service-name">24 hour emergency service</span></div>
    <div class="service col-1 row-2"><div class="service-tile" role="img" aria-label="Wrench and hammer icon"><svg viewBox="0 0 40 40"><path class="ico" d="M10 30L28 12M8 12a5 5 0 0 0 7 4l15 15M12 8l-4 4"/><path class="ico-fill" d="M24 8l8 8 2-2-8-8z"/></svg></div><span class="service-name">new installation</span></div>
    <div class="service col-1 row-3"><div class="service-tile" role="img" aria-label="House with wrench icon"><svg viewBox="0 0 40 40"><path class="ico" d="M6 19L20 7l14 12M10 16v17h20V16M14 29l10-10M23 17a3 3 0 1 0 3 3"/></svg></div><span class="service-name">repairs</span></div>
    <div class="service col-1 row-4"><div class="service-tile" role="img" aria-label="House maintenance icon"><svg viewBox="0 0 40 40"><path class="ico-fill" d="M20 6L4 20h4v14h24V20h4z"/><path class="ico" style="stroke:#4fc3f1" d="M14 28l6-6M22 20a3 3 0 1 0 3-3M26 26v5"/></svg></div><span class="service-name">maintenance</span></div>
    <div class="service col-1 row-5"><div class="service-tile" role="img" aria-label="Paint roller and house icon"><svg viewBox="0 0 40 40"><rect class="ico-fill" x="5" y="5" width="16" height="7" rx="2"/><path class="ico" d="M21 8h3v7h-11v6"/><path class="ico-fill" d="M11 21h4v9h-4zM26 20l-9 8h3v6h12v-6h3z"/></svg></div><span class="service-name">renovations/extensions</span></div>
    <div class="service col-1 row-6"><div class="service-tile" role="img" aria-label="Cable icon"><svg viewBox="0 0 40 40"><path class="ico" style="stroke-width:6" d="M8 34L24 14"/><path class="ico" d="M24 14l4-8M25 15l7-5M25 16l8 0M24 14l0-8"/></svg></div><span class="service-name">re-wiring</span></div>

    <div class="service col-2 row-1"><div class="service-tile" role="img" aria-label="Home theatre icon"><svg viewBox="0 0 40 40"><rect class="ico" x="6" y="7" width="28" height="8" rx="1"/><rect class="ico" x="13" y="18" width="14" height="9"/><path class="ico" d="M4 30h32M6 30v4M34 30v4M6 17v10M34 17v10"/></svg></div><span class="service-name">home theatre</span></div>
    <div class="service col-2 row-2"><div class="service-tile" role="img" aria-label="Speakers icon"><svg viewBox="0 0 40 40"><rect class="ico" x="3" y="9" width="10" height="22" rx="1"/><rect class="ico" x="27" y="9" width="10" height="22" rx="1"/><circle class="ico" cx="8" cy="24" r="3"/><circle class="ico" cx="32" cy="24" r="3"/><rect class="ico" x="15" y="18" width="10" height="9"/></svg></div><span class="service-name">surround sound</span></div>
    <div class="service col-2 row-3"><div class="service-tile" role="img" aria-label="Wall television icon"><svg viewBox="0 0 40 40"><rect class="ico" x="5" y="13" width="30" height="20" rx="2"/><rect class="ico" x="9" y="17" width="22" height="12"/><path class="ico" d="M16 13l-3-6h5"/></svg></div><span class="service-name">wall tv’s</span></div>
    <div class="service col-2 row-4"><div class="service-tile" role="img" aria-label="Shower icon"><svg viewBox="0 0 40 40"><path class="ico" d="M22 14l8-8h5"/><path class="ico-fill" d="M14 14l10 10 2-6-6-6z"/><path class="ico" d="M14 24l-3 3M10 22l-4 2M17 27l-2 4M11 30l-3 3M6 28l-2 1"/></svg></div><span class="service-name">electric hot water</span></div>
    <div class="service col-2 row-5"><div class="service-tile" role="img" aria-label="Pot on stove icon"><svg viewBox="0 0 40 40"><path class="ico" d="M16 4c-1 2 1 2 0 4M20 4c-1 2 1 2 0 4M24 4c-1 2 1 2 0 4M8 14h24M11 14v10h18V14M6 17h5M29 17h5M9 26v10h22V26"/><path class="ico-fill" d="M20 28c-3 3-2 6 0 6s3-3 0-6z"/></svg></div><span class="service-name">stoves</span></div>
    <div class="service col-2 row-6"><div class="service-tile" role="img" aria-label="Oven icon"><svg viewBox="0 0 40 40"><rect class="ico" x="8" y="4" width="24" height="32" rx="2"/><path class="ico" d="M8 12h24M13 8h2M19 8h2M25 8h2"/><rect class="ico" x="12" y="17" width="16" height="13"/></svg></div><span class="service-name">cooktops</span></div>

    <div class="service col-3 row-1"><div class="service-tile" role="img" aria-label="Ceiling fan and light icon"><svg viewBox="0 0 40 40"><path class="ico" d="M16 4v7"/><path class="ico-fill" d="M10 18a6 6 0 0 1 12 0z"/><path class="ico" d="M14 22l-2 3M18 22l2 3"/><circle class="ico-fill" cx="28" cy="26" r="2.5"/><path class="ico-fill" d="M28 26l-12 4 1 3zM28 26l8-10 2 2zM28 26l4 10-3 1z"/></svg></div><span class="service-name">lighting &amp; ceiling fans</span></div>
    <div class="service col-3 row-2"><div class="service-tile" role="img" aria-label="Plug with tick icon"><svg viewBox="0 0 40 40"><path class="ico" d="M17 10a11 11 0 1 0 0 20M8 16h4M8 24h4M12 13h6v14h-6z"/><circle class="ico" cx="27" cy="22" r="8"/><path class="ico" d="M23 22l3 3 7-9"/></svg></div><span class="service-name">testing and tagging</span></div>
    <div class="service col-3 row-3"><div class="service-tile" role="img" aria-label="Server rack icon"><svg viewBox="0 0 40 40"><rect class="ico-fill" x="7" y="5" width="26" height="8" rx="1"/><rect class="ico-fill" x="7" y="16" width="26" height="8" rx="1"/><rect class="ico-fill" x="7" y="27" width="26" height="8" rx="1"/><path class="ico" style="stroke:#4fc3f1" d="M11 9h4M11 20h4M11 31h4"/></svg></div><span class="service-name">data</span></div>
    <div class="service col-3 row-4"><div class="service-tile" role="img" aria-label="Telephone icon"><svg viewBox="0 0 40 40"><path class="ico-fill" d="M4 14c0-4 7-6 16-6s16 2 16 6v3h-8v-3c-3-1-13-1-16 0v3H4z"/><path class="ico-fill" d="M10 20h20l4 14H6z"/><circle class="ico" style="stroke:#4fc3f1" cx="20" cy="27" r="4"/></svg></div><span class="service-name">telephone</span></div>
    <div class="service col-3 row-5"><div class="service-tile" role="img" aria-label="Security camera icon"><svg viewBox="0 0 40 40"><path class="ico-fill" d="M4 12l24 8-3 7L2 19z"/><path class="ico" d="M22 26l2 5h8M32 26v10"/><circle class="ico-fill" cx="30" cy="19" r="2"/></svg></div><span class="service-name">security systems</span></div>
  </section>

  <p class="sectors">We Serve <em>RESIDENTIAL</em>, <em>COMMERCIAL</em> and <em>INDUSTRIAL</em> Sectors.</p>

  <footer class="contact-bar">
    <span class="call-label">Call us:</span>
    <span class="call-number">0000 000 000</span>
    <span class="website">www.harborquilldune.com.au</span>
  </footer>

  <div class="brand">
    <span class="brand-dot"></span>
    <span class="brand-name">Harbor Quill Dune Electrical and Security</span>
  </div>
</main>
</body>
</html>
```